new marketing company logo and business card

design logo and biz card for marketing start up.

My company name needs a brand logo designed: Copper Lantern Marketing Co.
Tagline: Sales - Marketing - Brand Building

Sister Bay is the name of my favorite place, in Wisconsin, but the business is NOT BASED there. It should evoke warmth, friendliness, professionalism, and marketing services from a seasoned marketer.

Target Market(s)

I am selling my services to small business that need help.

Industry/Entity Type

Marketing

Contact Information for Business Card

Copper Lantern Marketing Co. (logo)
Sales - Marketing - Brand Building (tagline)

Dana M. Whitcombe
DanaMWhitcombe@fernlymail.com
555-384-0192 mobile

Font styles to use
Serif
Sans Serif

Colors
f78f20
f37122
f68d4d
00a990
85cae6
33b8a4
faa54b

Requirements
Must have
• a logo
• a business card
Nice to have
• I'd love to see a small subtle reference to Sister Bay built in. Sister bay is named that because there are two islands called ‘sister islands’ that flank the bay. If you google this you will see.
• I like warm, earthy colors. But, I am a fun, approachable, real person. Not stand-offish. Should be warm and appealing yet professional.
Should not have
• nothing cartoon-ish. no child-like fonts. this is a professional business.

```html
<!DOCTYPE html>
<html lang="en">
<head>
<meta charset="utf-8">
<title>Copper Lantern Marketing Co. – Business Card</title>
<link rel="stylesheet" href="https://fonts.googleapis.com/css2?family=Arimo:wght@400&family=Nunito:wght@400;700&display=swap">
<style>
  :root {
    --backdrop: #e8e9eb;
    --paper: #ffffff;
    --teal: #28bba0;
    --orange: #f59229;
    --orange-rule: #f37122;
    --ink-grey: #8a8c8f;
    --white: #ffffff;
  }
  * { margin: 0; padding: 0; box-sizing: border-box; }
  html, body {
    width: 960px; height: 1200px; overflow: hidden;
    background: var(--backdrop);
  }
  .canvas { position: relative; width: 960px; height: 1200px; }

  .sheet {
    position: absolute; left: 60px; width: 840px; height: 480px;
    background: var(--paper);
  }
  .sheet--front { top: 94px; }
  .sheet--back { top: 626px; }

  .card {
    position: absolute; left: 204px; top: 0; width: 432px; height: 480px;
  }

  /* front */
  .brand-block {
    position: absolute; left: 0; top: 0; width: 432px; height: 274px;
    background: var(--teal); color: var(--white); text-align: center;
  }
  .brand-name {
    position: absolute; left: 0; right: 0; top: 110px;
    font-family: "Nunito", sans-serif; font-weight: 700;
    font-size: 34px; line-height: 38px; letter-spacing: 0.5px;
  }
  .brand-rule {
    position: absolute; left: 190px; top: 236px; width: 52px; height: 2px;
    background: var(--orange-rule);
  }
  .tagline {
    position: absolute; left: 0; right: 0; top: 243px;
    font-family: "Nunito", sans-serif; font-weight: 400; font-size: 13px;
  }

  .contact {
    position: absolute; left: 0; right: 0; top: 286px; text-align: center;
    font-family: "Arimo", sans-serif; font-weight: 400;
  }
  .contact__name { color: var(--teal); font-size: 35px; line-height: 40px; }
  .contact__line { color: var(--ink-grey); font-size: 25px; line-height: 35px; }

  .accent-bar {
    position: absolute; left: 0; bottom: 0; width: 432px; height: 35px;
    background: var(--orange);
  }

  /* back */
  .card--back { background: var(--orange); }
  .back-name {
    position: absolute; left: 0; right: 0; top: 196px; text-align: center;
    color: var(--white);
    font-family: "Nunito", sans-serif; font-weight: 700;
    font-size: 38px; line-height: 44px;
  }
</style>
</head>
<body>
<main class="canvas">
  <section class="sheet sheet--front">
    <div class="card card--front">
      <div class="brand-block">
        <div class="brand-name">Copper Lantern<br>Marketing Co.</div>
        <div class="brand-rule"></div>
        <div class="tagline">Sales - Marketing - Brand Building</div>
      </div>
      <div class="contact">
        <p class="contact__name">Dana M. Whitcombe</p>
        <p class="contact__line">DanaMWhitcombe@fernlymail.com</p>
        <p class="contact__line">555-384-0192</p>
        <p class="contact__line">copperlanternmarketing.com</p>
      </div>
      <div class="accent-bar"></div>
    </div>
  </section>

  <section class="sheet sheet--back">
    <div class="card card--back">
      <div class="back-name">Copper Lantern<br>Marketing Co.</div>
    </div>
  </section>
</main>
</body>
</html>
```